business card with 2 locations on 1 card

I need a modern looking business card that I would use at 2 different locations. Possibly 1 location on 1 side and other location on other side. One should be able to distinguish the 2 locations immediately before having to read the address or description on card. You can take a look at my website to see what I'm drawn to. The logo is brand new that I just purchased on Craft Hive. I want to emphasize family.
Updates

Let's not use the yellow and blue colors. Added Thursday, August 31, 2017

Target Market(s)

women and children

Industry/Entity Type

Health And Wellness

Contact Information for Business Card

Business name: Willow Brook Chiropractic & Acupuncture
My name: Lorin Daske
Job title: DC, MAOM, LAc (CA), CNS

Location 1
Address: 4817 Marlowe Blvd, Suite B-100, Frisco, TX 75034
Phone: (469) 555-0182
Fax: (972) 555-0137

Location 2
Address: 1936 Belvane Road, Suite 100, Plano, TX 75075
Phone: (469) 555-0169
Fax: (972) 555-0137

Email: drlorindaske@mailnest.example
Website: www.drlorindaske.example

Font styles to use
Serif
Sans Serif

Colors

Designer to choose colors to be used in the design.

Requirements
Must have
• distinction between 2 locations.
Nice to have
• Colors preference below is there. But I like to see what you come up with too!

```html
<!DOCTYPE html>
<html lang="en">
<head>
<meta charset="utf-8">
<title>Willow Brook Chiropractic &amp; Acupuncture – Business Card</title>
<link href="https://fonts.googleapis.com/css2?family=Arimo:wght@400;700&display=swap" rel="stylesheet">
<style>
  :root{
    --backdrop:#ece6de;
    --card:#f7f7f5;
    --card-edge:#e2e1dc;
    --teal:#2f7f76;
    --leaf:#8cc63f;
    --green:#1f9a3e;
    --ink:#2a2a2a;
    --icon:#d9534f;
  }
  *{margin:0;padding:0;box-sizing:border-box}
  html,body{width:1200px;height:729px;overflow:hidden;background:var(--backdrop)}
  .canvas{position:relative;width:1200px;height:729px}
  .card{
    position:absolute;width:520px;height:297px;background:var(--card);
    border:1px solid var(--card-edge);border-radius:3px;
    box-shadow:0 6px 18px rgba(80,60,40,.12);
  }
  .card--details{left:50px;top:216px}
  .card--front{left:630px;top:216px}

  .brand{display:flex;align-items:center;gap:14px}
  .brand__dot{flex:none;border-radius:50%;background:var(--leaf)}
  .brand__name{font-family:"Arimo",sans-serif;font-weight:700;color:var(--teal);line-height:1.2}

  .card--front .brand{position:absolute;left:50px;top:106px}
  .card--front .brand__dot{width:84px;height:84px}
  .card--front .brand__name{font-size:21px;max-width:330px}

  .card--details .brand{position:absolute;left:30px;top:28px}
  .card--details .brand__dot{width:54px;height:54px}
  .card--details .brand__name{font-size:15px;max-width:230px}

  .location{position:absolute;font-family:"Arimo",sans-serif;font-size:11.5px;color:var(--ink);line-height:1.45}
  .location--plano{left:30px;top:110px}
  .location--frisco{left:282px;top:180px}
  .location__line{display:flex;align-items:center;gap:6px}
  .location__line--address{padding-left:19px}
  .icon{width:13px;height:13px;flex:none}

  .person{position:absolute;right:30px;top:100px;text-align:right;font-family:"Arimo",sans-serif}
  .person__name{font-weight:700;font-size:30px;color:var(--green);letter-spacing:-.3px}
  .person__title{font-size:10.5px;color:var(--green);margin-top:2px}
</style>
</head>
<body>
<div class="canvas">

  <section class="card card--details">
    <div class="brand">
      <span class="brand__dot"></span>
      <span class="brand__name">Willow Brook Chiropractic &amp; Acupuncture</span>
    </div>

    <div class="location location--plano">
      <div class="location__line location__line--address">1936 Belvane Road,</div>
      <div class="location__line location__line--address">Suite 100, Plano, TX 75075</div>
      <div class="location__line"><svg class="icon" viewBox="0 0 13 13"><rect width="13" height="13" rx="2" fill="var(--icon)"/><path d="M4 3h2l.6 2-1.2.8a5 5 0 0 0 1.8 1.8L8 6.4l2 .6v2A1 1 0 0 1 9 10 6 6 0 0 1 3 4a1 1 0 0 1 1-1z" fill="#fff"/></svg>(469) 555-0169</div>
      <div class="location__line"><svg class="icon" viewBox="0 0 13 13"><rect width="13" height="13" rx="2" fill="var(--icon)"/><rect x="3" y="5" width="7" height="4.5" fill="#fff"/><rect x="4.5" y="2.8" width="4" height="2.4" fill="#fff"/></svg>(972) 555-0137</div>
      <div class="location__line"><svg class="icon" viewBox="0 0 13 13"><rect width="13" height="13" rx="2" fill="var(--icon)"/><rect x="2.8" y="4" width="7.4" height="5" fill="#fff"/><path d="M2.8 4l3.7 3 3.7-3" stroke="var(--icon)" fill="none" stroke-width=".9"/></svg>drlorindaske@mailnest.example</div>
      <div class="location__line"><svg class="icon" viewBox="0 0 13 13"><circle cx="6.5" cy="6.5" r="6.5" fill="var(--icon)"/><circle cx="6.5" cy="6.5" r="3.6" fill="none" stroke="#fff" stroke-width="1"/><path d="M2.9 6.5h7.2M6.5 2.9v7.2" stroke="#fff" stroke-width=".8"/></svg>www.drlorindaske.example</div>
    </div>

    <div class="person">
      <div class="person__name">Lorin Daske</div>
      <div class="person__title">DC, MAOM, LAc (CA), CNS</div>
    </div>

    <div class="location location--frisco">
      <div class="location__line location__line--address">4817 Marlowe Blvd,</div>
      <div class="location__line location__line--address">Suite B-100, Frisco, TX 75034</div>
      <div class="location__line"><svg class="icon" viewBox="0 0 13 13"><rect width="13" height="13" rx="2" fill="var(--icon)"/><path d="M4 3h2l.6 2-1.2.8a5 5 0 0 0 1.8 1.8L8 6.4l2 .6v2A1 1 0 0 1 9 10 6 6 0 0 1 3 4a1 1 0 0 1 1-1z" fill="#fff"/></svg>(469) 555-0182</div>
      <div class="location__line"><svg class="icon" viewBox="0 0 13 13"><rect width="13" height="13" rx="2" fill="var(--icon)"/><rect x="3" y="5" width="7" height="4.5" fill="#fff"/><rect x="4.5" y="2.8" width="4" height="2.4" fill="#fff"/></svg>(972) 555-0137</div>
      <div class="location__line"><svg class="icon" viewBox="0 0 13 13"><rect width="13" height="13" rx="2" fill="var(--icon)"/><rect x="2.8" y="4" width="7.4" height="5" fill="#fff"/><path d="M2.8 4l3.7 3 3.7-3" stroke="var(--icon)" fill="none" stroke-width=".9"/></svg>drlorindaske@mailnest.example</div>
      <div class="location__line"><svg class="icon" viewBox="0 0 13 13"><circle cx="6.5" cy="6.5" r="6.5" fill="var(--icon)"/><circle cx="6.5" cy="6.5" r="3.6" fill="none" stroke="#fff" stroke-width="1"/><path d="M2.9 6.5h7.2M6.5 2.9v7.2" stroke="#fff" stroke-width=".8"/></svg>www.drlorindaske.example</div>
    </div>
  </section>

  <section class="card card--front">
    <div class="brand">
      <span class="brand__dot"></span>
      <span class="brand__name">Willow Brook Chiropractic &amp; Acupuncture</span>
    </div>
  </section>

</div>
</body>
</html>
```